Redesign Business Cards, Attached

Please read instructions carefully. If you have any questions send a message before submitting your ONE design. Please redesign attached business cards. Double sided. Use same content and descriptions. Use black, silver, crimson red and gold colors. My only issue with the attached design is the background colors. I like the layout as-is. I can provide the individual pictures on the back side later. Do not submit more than one design. One submission shall include both front and back. Do not submit front and back separately. A second project will be launched to create a matching post card after completion of this.
Industry/Entity Type
see description and attachments.
Contact Information for Business Card
Requirements
Must have
- see description and attachments.
Nice to have
Should not have

```html
<!DOCTYPE html>
<html lang="en">
<head>
<meta charset="utf-8">
<title>Helm &amp; Harbor Boat Training — Business Card</title>
<link href="https://fonts.googleapis.com/css2?family=Open+Sans:wght@400;600;700;800&display=swap" rel="stylesheet">
<style>
  :root {
    --stage: #2a2b2e;
    --crimson: #b3232a;
    --crimson-deep: #8e1a20;
    --gold: #d2a62a;
    --ink: #111111;
    --paper: #ffffff;
    --text-dark: #1d1d1d;
    --sea-light: #dfe9f2;
    --sea-mid: #8fa9c2;
    --sea-deep: #3e5a78;
  }
  * { box-sizing: border-box; margin: 0; padding: 0; }
  html, body {
    width: 1200px; height: 952px; overflow: hidden;
    background: var(--stage);
    font-family: "Open Sans", Arial, sans-serif;
  }
  .canvas {
    position: relative; width: 1200px; height: 952px;
    display: flex; align-items: center; justify-content: center; gap: 40px;
  }
  .card {
    position: relative; width: 540px; height: 310px;
    border-radius: 18px; overflow: hidden;
    box-shadow: 0 14px 30px rgba(0,0,0,.45);
  }
  .card-shapes { position: absolute; inset: 0; }

  /* Front */
  .card--front { background: var(--paper); }
  .brand {
    position: absolute; left: 40px; top: 26px;
    display: flex; align-items: center; gap: 8px;
    font-size: 13px; font-weight: 700; color: var(--ink);
    letter-spacing: .04em; text-transform: uppercase;
  }
  .brand-dot { width: 16px; height: 16px; border-radius: 50%; background: var(--gold); }
  .holder-name {
    position: absolute; left: 40px; top: 78px;
    font-size: 27px; font-weight: 700; text-transform: uppercase; letter-spacing: .01em;
    color: var(--crimson);
  }
  .holder-name .surname { color: var(--gold); }
  .holder-title {
    position: absolute; left: 40px; top: 118px; width: 300px;
    font-size: 13.5px; line-height: 1.3; color: var(--text-dark);
  }
  .phone {
    position: absolute; left: 40px; top: 184px;
    font-size: 19px; font-weight: 700; color: var(--paper); letter-spacing: .01em;
  }
  .contact-list {
    position: absolute; left: 40px; top: 218px; list-style: none;
    font-size: 11.5px; color: var(--paper); line-height: 17px;
  }
  .contact-list li { display: flex; align-items: center; gap: 6px; }
  .contact-icon { width: 13px; height: 13px; }

  /* Back */
  .card--back { background: linear-gradient(135deg, #c0272e 0%, var(--crimson) 55%, #a21f25 100%); }
  .services {
    position: absolute; left: 232px; top: 104px; list-style: none;
    font-size: 14.5px; font-weight: 600; color: var(--paper); line-height: 22px;
  }
  .services li { position: relative; padding-left: 13px; }
  .services li::before {
    content: ""; position: absolute; left: 0; top: 8px;
    width: 6px; height: 6px; border-radius: 50%; background: var(--gold);
  }
</style>
</head>
<body>
<main class="canvas">

  <section class="card card--front" aria-label="Business card front">
    <svg class="card-shapes" width="540" height="310" viewBox="0 0 540 310">
      <defs>
        <linearGradient id="sea" x1="0" y1="0" x2="1" y2="1">
          <stop offset="0" stop-color="var(--sea-light)"/>
          <stop offset=".55" stop-color="var(--sea-mid)"/>
          <stop offset="1" stop-color="var(--sea-deep)"/>
        </linearGradient>
      </defs>
      <path class="band band--red" d="M0 176 H372 V212 H0 Z" fill="var(--crimson)"/>
      <path class="band band--black" d="M0 212 H372 V254 H0 Z" fill="var(--ink)"/>
      <path class="gold-sweep" d="M540 200 V310 H330 V246 Q330 214 362 206 L400 198 Q420 194 440 220 L470 256 Q484 272 504 262 Z" fill="var(--gold)"/>
      <path class="photo-frame" d="M372 70 H540 V248 L500 272 Q484 282 470 266 L392 176 Q372 154 372 128 Z" fill="var(--paper)"/>
      <path d="M380 64 H540 V252 L502 276 Q484 286 468 268 L388 178 Q366 154 366 128 V78 Q366 64 380 64 Z" fill="none" stroke="var(--crimson)" stroke-width="5"/>
      <path role="img" aria-label="Photo: motor boat cruising across open water, seen from above"
            d="M386 74 H540 V246 L500 270 Q486 278 474 264 L396 176 Q376 154 376 130 V84 Q376 74 386 74 Z"
            fill="url(#sea)"/>
    </svg>

    <div class="brand"><span class="brand-dot"></span>Helm &amp; Harbor Boat Training</div>
    <h1 class="holder-name">Jordan T. <span class="surname">Halvek</span></h1>
    <p class="holder-title">USCG Licensed Captain Certified<br>Instructor</p>
    <p class="phone">TEXT (555) 014-2290</p>
    <ul class="contact-list">
      <li>
        <svg class="contact-icon" viewBox="0 0 13 13"><rect width="13" height="13" rx="2" fill="var(--gold)"/><path d="M2.5 4 H10.5 V9.5 H2.5 Z M2.5 4 L6.5 7 L10.5 4" fill="none" stroke="var(--ink)" stroke-width="1"/></svg>
        hello@helmcrew.com
      </li>
      <li>
        <svg class="contact-icon" viewBox="0 0 13 13"><rect width="13" height="13" rx="2" fill="var(--gold)"/><circle cx="6.5" cy="6.5" r="4" fill="none" stroke="var(--ink)" stroke-width="1"/><path d="M2.5 6.5 H10.5 M6.5 2.5 Q4 6.5 6.5 10.5 Q9 6.5 6.5 2.5" fill="none" stroke="var(--ink)" stroke-width=".8"/></svg>
        www.HelmCrew.com
      </li>
    </ul>
  </section>

  <section class="card card--back" aria-label="Business card back">
    <svg class="card-shapes" width="540" height="310" viewBox="0 0 540 310">
      <defs>
        <radialGradient id="anchorGlow" cx=".5" cy=".5" r=".5">
          <stop offset="0" stop-color="var(--crimson-deep)" stop-opacity=".75"/>
          <stop offset=".7" stop-color="var(--crimson-deep)" stop-opacity=".35"/>
          <stop offset="1" stop-color="var(--crimson-deep)" stop-opacity="0"/>
        </radialGradient>
      </defs>
      <ellipse role="img" aria-label="Faint decoration: ship anchor wrapped in rope"
               cx="130" cy="130" rx="140" ry="125" fill="url(#anchorGlow)"/>
    </svg>
    <ul class="services">
      <li>Hands-On Boat Training</li>
      <li>Introduction to Power Boating</li>
      <li>Precision Docking &amp; Boat Handling</li>
      <li>Open Water Boat Handling</li>
      <li>Island Anchoring</li>
      <li>Open Water Advanced Maneuvers</li>
      <li>Coastal Navigation</li>
      <li>Captaining/ Piloting Service for<br>Your Outings</li>
    </ul>
  </section>

</main>
</body>
</html>
```